Web design for TRADEBACKS. A forex rebate platform website

I need a complete design for a forex rebate website called TRADEBACKS. The website will include the following pages:

- Homepage
- Broker Listing Page
- Broker Rebate Detail Page

Please review the attached file for detailed requirements and the content that needs to be designed.

Number of Pages Required

3 page

```html
<!DOCTYPE html>
<html lang="en">
<head>
<meta charset="utf-8">
<title>TRADEBACKS – Page Designs</title>
<link href="https://fonts.googleapis.com/css2?family=Inter:wght@400;500;600;700;800;900&display=swap" rel="stylesheet">
<style>
:root{
  --board:#efefef;
  --label:#a3a3a3;
  --white:#ffffff;
  --ink:#0b0d12;
  --text:#1f2430;
  --muted:#7a808c;
  --line:#e4e6ea;
  --soft:#f5f6f8;
  --blue:#1466f0;
  --blue-soft:#e7f0ff;
  --navy:#0a1322;
  --navy-2:#141d2d;
  --navy-3:#1c2638;
  --green:#1fbf63;
  --green-soft:#e4f8ec;
}
*{box-sizing:border-box;margin:0;padding:0}
html,body{width:1200px;height:610px;overflow:hidden}
body{background:var(--board);font-family:'Inter',sans-serif;color:var(--text);position:relative}
.a{position:absolute}
.board-label{position:absolute;top:35px;font-size:9.5px;color:var(--label);font-weight:500}
.page{position:absolute;top:51px;width:365px;background:var(--white);overflow:hidden}
.page--home{left:64px;height:559px}
.page--detail{left:436px;height:559px}
.page--listing{left:809px;height:544px}

/* nav */
.nav{position:absolute;left:0;top:0;width:100%;height:19px;background:var(--white)}
.nav__logo{position:absolute;left:31px;top:6px;font-size:7.5px;font-weight:800;color:var(--ink);letter-spacing:-.2px}
.nav__links{position:absolute;left:149px;top:8px;display:flex;gap:7px;font-size:3.4px;color:var(--text)}
.nav__links .is-active{color:var(--blue);font-weight:600}
.nav__right{position:absolute;right:31px;top:6px;display:flex;align-items:center;gap:7px;font-size:3.6px;font-weight:600}
.btn-pill{background:var(--ink);color:#fff;border-radius:6px;padding:2px 6px;font-size:3.5px;font-weight:600}

.t{font-size:3.6px;line-height:1.45;color:var(--muted)}
.t-dark{color:var(--ink)}
.bold{font-weight:700}

/* home */
.hero-title{left:31px;top:44px;font-size:18px;line-height:17px;font-weight:900;color:var(--ink);letter-spacing:-.4px}
.hero-title .accent{color:var(--blue)}
.btn{position:absolute;height:10px;border-radius:5px;font-size:3.4px;font-weight:600;display:flex;align-items:center;justify-content:center}
.btn--dark{background:var(--ink);color:#fff}
.btn--ghost{border:.6px solid #cfd3da;color:var(--ink);background:#fff}
.btn--blue{background:var(--blue);color:#fff}
.btn--outline-light{border:.6px solid #3a465c;color:#fff}
.hero-visual{left:180px;top:44px;width:166px;height:122px;border-radius:6px;background:linear-gradient(135deg,#f4f5f7,#e1e4e9)}
.stat__value{font-size:11px;font-weight:800;color:var(--ink);letter-spacing:-.3px}
.stat__label{font-size:2.8px;color:var(--muted);letter-spacing:.2px;margin-top:2px}
.flow-section{left:0;top:255px;width:100%;height:218px;background:var(--soft)}
.section-title{font-size:11px;font-weight:800;color:var(--ink);letter-spacing:-.2px}
.flow-line{left:109.5px;top:92px;width:1px;height:100px;background:#c9cdd4}
.flow-node{width:25px;height:25px;border-radius:50%;background:#fff;border:.8px solid #d4d8de;display:flex;align-items:center;justify-content:center}
.flow-node--blue{border-color:#9ec0f6}
.flow-node--black{background:var(--ink);border-color:var(--ink)}
.flow-node--green{border-color:#8fdcb0}
.flow-text{left:128px;width:140px}
.flow-text h4{font-size:5px;font-weight:700;color:var(--ink);margin-bottom:1px}
.tabs{display:flex;background:#f1f2f4;border-radius:6px;padding:1.5px}
.tabs span{font-size:3.2px;padding:2px 6px;border-radius:5px;color:var(--muted)}
.tabs .is-active{background:#fff;color:var(--ink);font-weight:600}
.tag-featured{background:var(--ink);color:#fff;font-size:2.6px;font-weight:700;padding:1px 4px;border-radius:4px}
.logo-chip{width:10px;height:10px;border-radius:2px;background:var(--ink)}

/* detail */
.detail-hero{left:0;top:19px;width:100%;height:118px;background:radial-gradient(circle at 335px 35px,#1c3b78 0,#0d1a33 30%,var(--navy) 60%)}
.code-box{left:31px;top:59px;width:146px;height:16px;border-radius:3px;background:#1b2538;border:.6px solid #2c374b}
.earn-card{left:223px;top:18px;width:79px;height:76px;border-radius:5px;background:#1a2232;border:.6px solid #2a3447}
.mini-box{background:#232c3d;border-radius:2px;height:15px}
.rate-row{left:46px;width:273px;height:18px;border:.6px solid var(--line);border-radius:3px;background:#fff}
.round-arrow{width:8px;height:8px;border-radius:50%;background:var(--ink)}
.calc-section{left:0;top:265px;width:100%;height:125px;background:var(--navy)}
.slider{height:1.4px;background:#3a4458;border-radius:1px}
.slider__fill{height:100%;background:#fff}
.knob{width:4px;height:4px;border-radius:50%;background:#fff;top:-1.3px}
.val-pill{background:var(--blue);color:#fff;font-size:3px;font-weight:700;padding:1px 3px;border-radius:2px}
.estimate-card{left:190px;top:23px;width:115px;height:78px;border-radius:6px;background:#182133;border:.6px solid #263046}
.info-section{left:0;top:390px;width:100%;height:113px;background:var(--soft)}
.info-card{top:22px;width:149px;height:68px;border-radius:4px;background:#fff;border:.6px solid var(--line)}
.info-card h5{font-size:5.4px;font-weight:700;color:var(--ink);padding:5px 5px 4px}
.info-row{display:flex;justify-content:space-between;align-items:center;padding:0 5px;height:11px;border-top:.6px solid var(--line);font-size:3px;color:var(--muted)}
.info-row b{color:var(--ink);font-weight:600}
.chip{font-size:2.4px;background:var(--blue-soft);color:var(--blue);padding:.5px 2px;border-radius:1.5px;margin-left:1px}
.pay-badge{top:542px;width:35px;height:14px;border-radius:3px;background:#f1f2f4;display:flex;align-items:center;justify-content:center}
.pay-badge i{width:8px;height:6px;background:#8ea0b4;border-radius:1px;display:block}

/* listing */
.float-card{background:#fff;border-radius:4px;box-shadow:0 2px 8px rgba(15,23,42,.1)}
.list-tabs{left:31px;top:121px;display:flex;gap:9px;font-size:3.2px;color:var(--muted)}
.list-tabs .is-active{color:var(--ink);font-weight:600;border-bottom:.8px solid var(--ink);padding-bottom:2px}
.sidebar-card{left:31px;width:62px;border:.6px solid var(--line);border-radius:3px;background:#fff}
.check{width:3px;height:3px;border-radius:.5px;background:var(--blue);display:inline-block;margin-right:2px;vertical-align:middle}
.check--off{background:#fff;border:.5px solid #b8bec8}
.broker-card{top:141px;width:74px;height:72px;border:.6px solid var(--line);border-radius:3px;background:#fff}
.rebate-box{background:#f2f4f7;border-radius:2px}
.table{left:102px;top:235px;width:231px;border:.6px solid var(--line);border-radius:3px;overflow:hidden;background:#fff}
.table__row{display:grid;grid-template-columns:40px 40px 36px 34px 40px 1fr;align-items:center;height:11.5px;border-top:.6px solid var(--line);font-size:2.7px;color:var(--text);padding-left:5px}
.table__row--head{background:#f6f7f9;border-top:0;color:var(--muted);font-size:2.4px;height:9px}
.cta{left:102px;top:300px;width:231px;height:59px;border-radius:4px;background:var(--navy)}
.footer-col h6{font-size:3px;font-weight:700;color:var(--ink);letter-spacing:.3px;margin-bottom:3px}
.footer-col p{font-size:2.9px;color:var(--muted);line-height:1.9}
</style>
</head>
<body>

<div class="board-label" style="left:64px">Home page</div>
<div class="board-label" style="left:436px">Broker Rebate Detail Page</div>
<div class="board-label" style="left:809px">Broker Listing Page</div>

<!-- HOME -->
<section class="page page--home">
  <nav class="nav">
    <div class="nav__logo">TRADEBACKS</div>
    <div class="nav__links"><span class="is-active">Find Brokers</span><span>Rebates</span><span>About</span><span>News</span></div>
    <div class="nav__right"><span>⊕ EN</span><span>Login</span><span class="btn-pill">Sign up</span></div>
  </nav>

  <h1 class="a hero-title">FOREX<br>REBATES<br>MADE SIMPLE.<br><span class="accent">UP TO 90%<br>BACK.</span></h1>
  <p class="a t" style="left:31px;top:139px;width:138px">Get paid for every trade you make. Connect your trading account to our partner brokers and start receiving daily cash rebates directly to your wallet.</p>
  <div class="btn btn--dark" style="left:31px;top:168px;width:47px">Start Earning Rebates</div>
  <div class="btn btn--ghost" style="left:81px;top:168px;width:42px">Compare Brokers</div>
  <div class="a hero-visual" role="img" aria-label="Dashboard on a tablet with floating cashback and earnings cards"></div>

  <div class="a" style="left:31px;top:205px;width:303px;height:.6px;background:var(--line)"></div>
  <div class="a" style="left:31px;top:214px"><div class="stat__value">$7.5M+</div><div class="stat__label">REBATES PAID</div></div>
  <div class="a" style="left:109px;top:214px"><div class="stat__value">15k+</div><div class="stat__label">ACTIVE TRADERS</div></div>
  <div class="a" style="left:188px;top:214px"><div class="stat__value">40+</div><div class="stat__label">SUPPORTED BROKERS</div></div>
  <div class="a" style="left:266px;top:214px"><div class="stat__value">24/7</div><div class="stat__label">PAYOUT FREQUENCY</div></div>

  <div class="a flow-section">
    <h2 class="a section-title" style="left:0;width:100%;text-align:center;top:21px">How The Cash Flows</h2>
    <p class="a t" style="left:107px;width:150px;text-align:center;top:41px">A transparent ecosystem built to maximize your returns. We cut out the noise so you keep the profit.</p>
    <div class="a flow-line"></div>
    <div class="a flow-node" style="left:97.5px;top:70px">
      <svg width="8" height="8" viewBox="0 0 16 16"><circle cx="8" cy="5" r="3" fill="none" stroke="#0b0d12" stroke-width="1.6"/><path d="M2 15c1-4 11-4 12 0" fill="none" stroke="#0b0d12" stroke-width="1.6"/></svg>
    </div>
    <div class="a flow-node flow-node--blue" style="left:97.5px;top:105px">
      <svg width="8" height="8" viewBox="0 0 16 16"><path d="M1 6 8 2l7 4M3 7v6M6.5 7v6M9.5 7v6M13 7v6M1 14h14" fill="none" stroke="#1466f0" stroke-width="1.5"/></svg>
    </div>
    <div class="a flow-node flow-node--black" style="left:97.5px;top:138px">
      <svg width="8" height="8" viewBox="0 0 16 16"><path d="M3 8h10M9 4l4 4-4 4" fill="none" stroke="#fff" stroke-width="1.8"/></svg>
    </div>
    <div class="a flow-node flow-node--green" style="left:97.5px;top:171px">
      <svg width="8" height="8" viewBox="0 0 16 16"><rect x="1.5" y="4" width="13" height="8" rx="1.5" fill="none" stroke="#1fbf63" stroke-width="1.5"/><circle cx="8" cy="8" r="1.8" fill="#1fbf63"/></svg>
    </div>
    <div class="a flow-text" style="top:72px"><h4>Trader</h4><p class="t">Executes Trades. You trade exactly as you normally would, with no changes to your spreads or execution speed.</p></div>
    <div class="a flow-text" style="top:107px"><h4 style="color:var(--blue)">Broker</h4><p class="t">Pays Commission. The broker pays us a volume-based commission for introducing your trading activity.</p></div>
    <div class="a flow-text" style="top:140px"><h4>TRADEBACKS</h4><p class="t">Processes Rebates. We take that commission, keep a small margin, and pass the majority straight back to you.</p></div>
    <div class="a flow-text" style="top:173px"><h4>Cashback</h4><p class="t">Paid to Wallet. Your cash arrives daily. Withdraw instantly via Crypto, PayWallet, or Bank Transfer.</p></div>
  </div>

  <h2 class="a section-title" style="left:61px;top:491px">Trusted Brokers</h2>
  <p class="a t" style="left:61px;top:510px">Partnering with industry leaders to give you the best rates.</p>
  <div class="a tabs" style="left:234px;top:507px"><span class="is-active">Forex</span><span>Prop Firms</span><span>Crypto</span></div>
  <div class="a tag-featured" style="left:106px;top:532px">★ FEATURED</div>
  <div class="a logo-chip" style="left:71px;top:547px"></div>
  <div class="a logo-chip" style="left:154px;top:547px"></div>
  <div class="a logo-chip" style="left:237px;top:547px"></div>
</section>

<!-- DETAIL -->
<section class="page page--detail">
  <nav class="nav">
    <div class="nav__logo">TRADEBACKS</div>
    <div class="nav__links"><span class="is-active">Find Brokers</span><span>Rebates</span><span>About</span><span>News</span></div>
    <div class="nav__right"><span>⊕ EN</span><span>Login</span><span class="btn-pill">Sign up</span></div>
  </nav>

  <div class="a detail-hero">
    <div class="a" style="left:31px;top:15px;width:11px;height:11px;border:1.2px solid #fff;border-radius:2px"></div>
    <div class="a" style="left:46px;top:15px;font-size:3.4px;color:#f5b400">★★★★★ <span style="color:#9aa3b2">15,000+ Traders</span></div>
    <div class="a" style="left:46px;top:20px;font-size:7px;font-weight:700;color:#fff">Harbor Markets</div>
    <div class="a" style="left:31px;top:34px;font-size:11px;line-height:12px;font-weight:800;color:#fff;letter-spacing:-.2px">Get Up To $8<br>Cashback Per Lot</div>
    <div class="a code-box">
      <div class="a" style="left:4px;top:2.5px;font-size:2.6px;color:#8a94a6">REFERRAL CODE</div>
      <div class="a" style="left:4px;top:7px;font-size:4.6px;font-weight:600;color:#fff;letter-spacing:.4px">TRADEBACKS2026</div>
      <div class="a" style="right:4px;top:5px;width:6px;height:6px;border-radius:1.5px;background:#323d52"></div>
    </div>
    <div class="btn btn--blue" style="left:31px;top:83px;width:46px;height:15px;border-radius:3px;text-align:center;line-height:1.3">Open New<br>Account</div>
    <div class="btn btn--outline-light" style="left:80px;top:83px;width:49px;height:15px;border-radius:3px;text-align:center;line-height:1.3">Link Existing<br>Account</div>

    <div class="a earn-card">
      <div class="a" style="left:6px;top:6px;font-size:3px;color:#9aa3b2">Total earnings</div>
      <div class="a" style="left:6px;top:10px;font-size:8px;font-weight:800;color:#fff">+$18.40</div>
      <div class="a" style="right:6px;top:6px;font-size:2.6px;font-weight:700;color:#0a1322;background:var(--green);padding:.5px 2px;border-radius:2px">+12.8%</div>
      <div class="a mini-box" style="left:6px;top:24px;width:32px"><div class="a" style="left:3px;top:2px;font-size:2.4px;color:#8a94a6">Rebates</div><div class="a" style="left:3px;top:6px;font-size:4.5px;font-weight:700;color:#fff">$422.90</div></div>
      <div class="a mini-box" style="left:41px;top:24px;width:32px"><div class="a" style="left:3px;top:2px;font-size:2.4px;color:#8a94a6">Volume</div><div class="a" style="left:3px;top:6px;font-size:4.5px;font-weight:700;color:#fff">$5,780.22</div></div>
      <svg class="a" style="left:6px;top:44px" width="67" height="27" viewBox="0 0 67 27">
        <rect x="1" y="17" width="7" height="10" fill="#3a4458"/><rect x="10" y="13" width="7" height="14" fill="#3a4458"/><rect x="19" y="15" width="7" height="12" fill="#3a4458"/><rect x="28" y="9" width="7" height="18" fill="#4a5570"/><rect x="37" y="6" width="7" height="21" fill="#5a6a8c"/><rect x="46" y="3" width="7" height="24" fill="#8aa2cf"/><rect x="55" y="0" width="7" height="27" fill="#dfe7f5"/>
      </svg>
    </div>
  </div>

  <h3 class="a" style="left:46px;top:159px;font-size:6.6px;font-weight:700;color:var(--ink)">Exclusive Rebate Rates</h3>
  <p class="a t" style="left:46px;top:168px;font-size:3px">Industry-leading cashback for every trade you execute.</p>
  <div class="a" style="left:288px;top:165px;font-size:2.8px;background:#eef0f3;padding:1px 3px;border-radius:2px;color:var(--ink)">Raw Spread Account</div>

  <div class="a rate-row" style="top:180px">
    <div class="a" style="left:5px;top:5px;width:7px;height:7px;border-radius:50%;background:#eef0f3"></div>
    <div class="a" style="left:16px;top:4px;font-size:3.6px;font-weight:700;color:var(--ink)">Forex Majors</div>
    <div class="a" style="left:16px;top:9.5px;font-size:2.6px;color:var(--muted)">EUR/USD, GBP/USD, USD/JPY</div>
    <div class="a" style="left:186px;top:4px;font-size:2.4px;color:var(--muted)">STANDARD</div>
    <div class="a" style="left:186px;top:8.5px;font-size:3.4px;color:var(--text)">$1.50 / Lot</div>
    <div class="a" style="left:228px;top:4px;font-size:2.4px;color:var(--blue)">REBATE</div>
    <div class="a" style="left:228px;top:8px;font-size:4.4px;font-weight:700;color:var(--blue)">$2.25 / Lot</div>
    <div class="a round-arrow" style="left:260px;top:5px"></div>
  </div>
  <div class="a rate-row" style="top:202px">
    <div class="a" style="left:5px;top:5px;width:7px;height:7px;border-radius:50%;background:#eef0f3"></div>
    <div class="a" style="left:16px;top:4px;font-size:3.6px;font-weight:700;color:var(--ink)">Precious Metals</div>
    <div class="a" style="left:16px;top:9.5px;font-size:2.6px;color:var(--muted)">XAU/USD, XAG/USD, Platinum</div>
    <div class="a" style="left:186px;top:4px;font-size:2.4px;color:var(--muted)">STANDARD</div>
    <div class="a" style="left:186px;top:8.5px;font-size:3.4px;color:var(--text)">$3.00 / Lot</div>
    <div class="a" style="left:228px;top:4px;font-size:2.4px;color:var(--blue)">REBATE</div>
    <div class="a" style="left:228px;top:8px;font-size:4.4px;font-weight:700;color:var(--blue)">$4.50 / Lot</div>
    <div class="a round-arrow" style="left:260px;top:5px"></div>
  </div>
  <div class="a rate-row" style="top:224px">
    <div class="a" style="left:5px;top:5px;width:7px;height:7px;border-radius:50%;background:#eef0f3"></div>
    <div class="a" style="left:16px;top:4px;font-size:3.6px;font-weight:700;color:var(--ink)">Cryptocurrencies</div>
    <div class="a" style="left:16px;top:9.5px;font-size:2.6px;color:var(--muted)">BTC, ETH, LTC, XRP</div>
    <div class="a" style="left:186px;top:4px;font-size:2.4px;color:var(--muted)">STANDARD</div>
    <div class="a" style="left:186px;top:8.5px;font-size:3.4px;color:var(--text)">5% of Spread</div>
    <div class="a" style="left:228px;top:4px;font-size:2.4px;color:var(--blue)">REBATE</div>
    <div class="a" style="left:228px;top:8px;font-size:4.4px;font-weight:700;color:var(--blue)">8% of Spread</div>
    <div class="a round-arrow" style="left:260px;top:5px"></div>
  </div>

  <div class="a calc-section">
    <h3 class="a" style="left:61px;top:32px;font-size:9.5px;font-weight:800;color:#fff">Estimate Your Profit</h3>
    <p class="a" style="left:61px;top:45px;width:90px;font-size:3px;line-height:1.5;color:#8a94a6">Use our transparent calculator to see how much you could earn back from your trading volume at this broker.</p>
    <div class="a" style="left:61px;top:63px;font-size:3.3px;font-weight:600;color:#fff">Daily Trading Volume (Lots)</div>
    <div class="a val-pill" style="left:149px;top:62px">10.0</div>
    <div class="a slider" style="left:61px;top:73px;width:101px"><div class="slider__fill" style="width:18%"></div><div class="a knob" style="left:16px"></div></div>
    <div class="a" style="left:61px;top:84px;font-size:3.3px;font-weight:600;color:#fff">Trading Days per Month</div>
    <div class="a val-pill" style="left:151px;top:83px">22</div>
    <div class="a slider" style="left:61px;top:94px;width:101px"><div class="slider__fill" style="width:76%"></div><div class="a knob" style="left:75px"></div></div>

    <div class="a estimate-card">
      <div class="a" style="left:0;width:100%;text-align:center;top:11px;font-size:2.8px;letter-spacing:.3px;color:#8a94a6">ESTIMATED MONTHLY REBATE</div>
      <div class="a" style="left:0;width:100%;text-align:center;top:16px;font-size:15px;font-weight:800;color:var(--green)">$495.00 <span style="font-size:6px">↗</span></div>
      <div class="a" style="left:10px;top:37px;width:95px;height:18px;border-radius:3px;background:#222c3f">
        <div class="a" style="left:5px;top:6px;font-size:5.5px;font-weight:700;color:#fff">$5,940.00</div>
        <div class="a" style="right:5px;top:5px;width:7px;height:7px;border-radius:1.5px;border:.6px solid var(--green)"></div>
      </div>
      <p class="a" style="left:12px;top:62px;width:91px;text-align:center;font-size:2.4px;line-height:1.5;color:#6e788a">Yearly total shown. Actual rebates depend on instrument mix and account type.</p>
    </div>
  </div>

  <div class="a info-section">
    <div class="a info-card" style="left:31px">
      <h5>ⓘ Broker Overview</h5>
      <div class="info-row"><span>Founded</span><b>2007</b></div>
      <div class="info-row"><span>Headquarters</span><b>Port Avalon</b></div>
      <div class="info-row"><span>Regulators</span><b><span class="chip">AUR</span><span class="chip">CYR</span><span class="chip">FSR</span></b></div>
      <div class="info-row"><span>Minimum Deposit</span><b>$200 USD</b></div>
    </div>
    <div class="a info-card" style="left:185px">
      <h5>⇅ Trading Conditions</h5>
      <div class="info-row"><span>Max Leverage</span><b>1:500</b></div>
      <div class="info-row"><span>Platforms</span><b>Desk4, Desk5, cDesk, ChartView</b></div>
      <div class="info-row"><span>Execution Type</span><b>ECN / DMA</b></div>
      <div class="info-row"><span>Strategies Allowed</span><b>Scalping, Hedging, EAs</b></div>
    </div>
  </div>

  <h3 class="a" style="left:0;width:100%;text-align:center;top:524px;font-size:6px;font-weight:700;color:var(--ink)">Fast Deposits &amp; Withdrawals</h3>
  <div class="a pay-badge" style="left:61px"><i></i></div>
  <div class="a pay-badge" style="left:103px"><i></i></div>
  <div class="a pay-badge" style="left:145px"><i></i></div>
  <div class="a pay-badge" style="left:187px"><i></i></div>
  <div class="a pay-badge" style="left:229px"><i></i></div>
  <div class="a pay-badge" style="left:271px"><i></i></div>
</section>

<!-- LISTING -->
<section class="page page--listing">
  <nav class="nav">
    <div class="nav__logo">TRADEBACKS</div>
    <div class="nav__links"><span class="is-active">Find Brokers</span><span>Rebates</span><span>About</span><span>News</span></div>
    <div class="nav__right"><span>⊕ EN</span><span>Login</span><span class="btn-pill">Sign up</span></div>
  </nav>

  <h1 class="a" style="left:31px;top:39px;font-size:11px;line-height:12px;font-weight:800;color:var(--ink);letter-spacing:-.2px">Compare Forex<br><span style="color:var(--blue)">Cashback Brokers</span></h1>
  <p class="a t" style="left:31px;top:67px;width:118px;font-size:3.2px">Maximize your trading returns by recovering the industry's highest rebate rates. We partner with top-tier brokers to put money back into your account on every trade.</p>
  <div class="a" style="left:31px;top:91px"><div style="font-size:6px;font-weight:800;color:var(--ink)">40+</div><div style="font-size:2.6px;color:var(--muted)">Verified Brokers</div></div>
  <div class="a" style="left:62px;top:91px"><div style="font-size:6px;font-weight:800;color:var(--ink)">15,000+</div><div style="font-size:2.6px;color:var(--muted)">Active Traders</div></div>
  <div class="a" style="left:99px;top:91px"><div style="font-size:6px;font-weight:800;color:var(--blue)">Up to 90%</div><div style="font-size:2.6px;color:var(--muted)">Cashback Rates</div></div>

  <div class="a float-card" style="left:206px;top:37px;width:48px;height:26px">
    <div class="a" style="left:4px;top:4px;font-size:2.6px;color:var(--muted)">Today's Cashback</div>
    <div class="a" style="left:4px;top:9px;font-size:6.5px;font-weight:800;color:var(--green)">+$28.45</div>
    <div class="a" style="left:4px;top:18px;font-size:2.2px;color:var(--green);background:var(--green-soft);padding:.5px 2px;border-radius:1px">↑ 12% FROM YESTERDAY</div>
  </div>
  <div class="a float-card" style="left:260px;top:37px;width:63px;height:57px">
    <div class="a" style="left:4px;top:4px;font-size:3px;font-weight:600;color:var(--ink)">Trading Volume</div>
    <div class="a" style="right:4px;top:4px;font-size:2.4px;color:var(--muted)">Last 7 Days</div>
    <svg class="a" style="left:4px;top:13px" width="55" height="38" viewBox="0 0 55 38"><path d="M0 34 C10 34 14 30 20 30 S30 30 34 18 S42 0 46 8 S52 30 55 30" fill="none" stroke="#1466f0" stroke-width="1.4"/></svg>
  </div>
  <div class="a float-card" style="left:213px;top:71px;width:55px;height:31px">
    <div class="a" style="left:4px;top:4px;font-size:2.6px;color:var(--muted)">Total Rebates</div>
    <div class="a" style="left:4px;top:8px;font-size:6.5px;font-weight:800;color:var(--blue)">+$642.80</div>
    <svg class="a" style="left:4px;top:18px" width="47" height="10" viewBox="0 0 47 10"><rect x="0" y="5" width="8" height="5" fill="#dbe7fb"/><rect x="10" y="3" width="8" height="7" fill="#c4d8fa"/><rect x="20" y="4" width="8" height="6" fill="#a9c6f7"/><rect x="30" y="1" width="8" height="9" fill="#6c9ff0"/><rect x="40" y="0" width="7" height="10" fill="#1466f0"/></svg>
  </div>
  <div class="a float-card" style="left:281px;top:89px;width:48px;height:16px">
    <div class="a" style="left:3px;top:4px;width:7px;height:7px;border-radius:1.5px;background:var(--ink)"></div>
    <div class="a" style="left:12px;top:3.5px;font-size:3px;font-weight:700;color:var(--ink)">Harbor Markets</div>
    <div class="a" style="left:12px;top:8px;font-size:2.4px;color:var(--green)">+$2.25 Rebate</div>
  </div>

  <div class="a list-tabs"><span class="is-active">▣ Forex Brokers</span><span>Prop Trading</span><span>Crypto Brokers</span></div>
  <div class="a" style="left:0;top:129.5px;width:100%;height:.6px;background:var(--line)"></div>

  <div class="a sidebar-card" style="top:141px;height:65px">
    <div class="a" style="left:4px;top:4px;font-size:3px;font-weight:700;color:var(--ink)">FILTERS</div>
    <div class="a" style="left:4px;top:9px;width:54px;height:5px;border:.5px solid var(--line);border-radius:1px;font-size:2.4px;color:var(--muted);padding-left:2px">Find by name...</div>
    <div class="a" style="left:4px;top:18px;font-size:2.4px;color:var(--muted);line-height:1.9">REGULATION<br><span class="check"></span><span style="color:var(--ink)">AUR (AU)</span><br><span class="check"></span><span style="color:var(--ink)">FCR (Global)</span><br><span class="check check--off"></span><span style="color:var(--ink)">CYR (EU)</span><br>ACCOUNT TYPE</div>
    <div class="a" style="left:4px;top:42px;display:flex;gap:2px"><span style="font-size:2.2px;background:var(--blue-soft);color:var(--blue);padding:.5px 2px;border-radius:1px">ECN</span><span style="font-size:2.2px;background:#f1f2f4;padding:.5px 2px;border-radius:1px">Raw</span><span style="font-size:2.2px;background:#f1f2f4;padding:.5px 2px;border-radius:1px">STP</span></div>
    <div class="a" style="left:4px;top:56px;font-size:2.4px;color:var(--blue)">View All Filters ›</div>
  </div>
  <div class="a sidebar-card" style="top:215px;height:90px">
    <div class="a" style="left:4px;top:4px;font-size:3px;font-weight:700;color:var(--ink)">▦ Rebate Calculator</div>
    <div class="a" style="left:4px;top:11px;font-size:2.4px;color:var(--muted)">Broker</div>
    <div class="a" style="left:4px;top:15px;width:54px;height:5px;border:.5px solid var(--line);border-radius:1px;font-size:2.4px;padding-left:2px;color:var(--ink)">Harbor Markets</div>
    <div class="a" style="left:4px;top:24px;font-size:2.4px;color:var(--muted)">Lots / Month</div><div class="a" style="right:4px;top:24px;font-size:2.4px;color:var(--ink)">50</div>
    <div class="a slider" style="left:4px;top:29px;width:54px;background:#e3e6ea"><div class="slider__fill" style="width:20%;background:var(--blue)"></div></div>
    <div class="a" style="left:4px;top:34px;font-size:2.4px;color:var(--muted)">Rebate Per Lot</div><div class="a" style="right:4px;top:34px;font-size:2.4px;color:var(--ink)">$8</div>
    <div class="a slider" style="left:4px;top:39px;width:54px;background:#e3e6ea"><div class="slider__fill" style="width:40%;background:var(--blue)"></div></div>
    <div class="a" style="left:4px;top:45px;width:54px;height:17px;border-radius:2px;background:var(--green-soft)">
      <div class="a" style="left:3px;top:3px;font-size:2.4px;color:var(--muted)">Monthly Rebate</div><div class="a" style="right:3px;top:2.5px;font-size:3.4px;font-weight:700;color:var(--green)">$420.00</div>
      <div class="a" style="left:3px;top:10px;font-size:2.4px;color:var(--muted)">Yearly Potential</div><div class="a" style="right:3px;top:9.5px;font-size:3px;font-weight:700;color:var(--ink)">$5,040.00</div>
    </div>
    <div class="a" style="left:4px;top:68px;width:54px;height:7px;border-radius:1.5px;background:var(--ink);color:#fff;font-size:2.6px;font-weight:600;display:flex;align-items:center;justify-content:center">Claim This Rebate</div>
  </div>

  <div class="a broker-card" style="left:102px">
    <div class="a" style="left:5px;top:5px;width:13px;height:13px;border-radius:2px;background:var(--ink)"></div>
    <div class="a" style="right:5px;top:5px;font-size:2.2px;color:var(--blue);background:var(--blue-soft);padding:.5px 2px;border-radius:1px">TOP VERIFIED</div>
    <div class="a" style="left:5px;top:21px;font-size:4.5px;font-weight:700;color:var(--ink)">Harbor Markets</div>
    <div class="a" style="left:5px;top:27px;font-size:2.4px;color:#f5b400">★★★★★ <span style="color:var(--muted)">4.8 (2.4k)</span></div>
    <div class="a rebate-box" style="left:5px;top:33px;width:64px;height:17px"><div class="a" style="left:3px;top:3px;font-size:2.2px;color:var(--muted)">Max Rebate</div><div class="a" style="left:3px;top:7px;font-size:5px;font-weight:800;color:var(--blue)">Up to $1.50 <span style="font-size:2.4px;color:var(--muted);font-weight:400">/ Lot</span></div></div>
    <div class="a" style="left:5px;top:53px;display:flex;gap:1.5px"><span class="chip">AUR</span><span class="chip">CYR</span><span class="chip">FSR</span></div>
    <div class="a" style="left:5px;top:60px;width:20px;height:6px;border:.5px solid var(--line);border-radius:1px;font-size:2.2px;display:flex;align-items:center;justify-content:center">Details</div>
    <div class="a" style="right:5px;top:60px;width:22px;height:6px;background:var(--blue);border-radius:1px;font-size:2.2px;color:#fff;display:flex;align-items:center;justify-content:center">Add Account</div>
  </div>
  <div class="a broker-card" style="left:181px">
    <div class="a" style="left:5px;top:5px;width:13px;height:13px;border-radius:2px;background:var(--ink)"></div>
    <div class="a" style="left:5px;top:21px;font-size:4.5px;font-weight:700;color:var(--ink)">Novexa</div>
    <div class="a" style="left:5px;top:27px;font-size:2.4px;color:#f5b400">★★★★★ <span style="color:var(--muted)">4.7 (1.9k)</span></div>
    <div class="a rebate-box" style="left:5px;top:33px;width:64px;height:17px"><div class="a" style="left:3px;top:3px;font-size:2.2px;color:var(--muted)">Max Rebate</div><div class="a" style="left:3px;top:7px;font-size:5px;font-weight:800;color:var(--blue)">Up to 33% <span style="font-size:2.4px;color:var(--muted);font-weight:400">Spread</span></div></div>
    <div class="a" style="left:5px;top:60px;width:20px;height:6px;border:.5px solid var(--line);border-radius:1px;font-size:2.2px;display:flex;align-items:center;justify-content:center">Details</div>
    <div class="a" style="right:5px;top:60px;width:22px;height:6px;background:var(--blue);border-radius:1px;font-size:2.2px;color:#fff;display:flex;align-items:center;justify-content:center">Add Account</div>
  </div>
  <div class="a broker-card" style="left:259px">
    <div class="a" style="left:5px;top:5px;width:13px;height:13px;border-radius:2px;background:var(--ink)"></div>
    <div class="a" style="left:5px;top:21px;font-size:4.5px;font-weight:700;color:var(--ink)">Tidewell</div>
    <div class="a" style="left:5px;top:27px;font-size:2.4px;color:#f5b400">★★★★★ <span style="color:var(--muted)">4.6 (1.2k)</span></div>
    <div class="a rebate-box" style="left:5px;top:33px;width:64px;height:17px"><div class="a" style="left:3px;top:3px;font-size:2.2px;color:var(--muted)">Max Rebate</div><div class="a" style="left:3px;top:7px;font-size:5px;font-weight:800;color:var(--blue)">Up to $2.00 <span style="font-size:2.4px;color:var(--muted);font-weight:400">/ Lot</span></div></div>
    <div class="a" style="left:5px;top:60px;width:20px;height:6px;border:.5px solid var(--line);border-radius:1px;font-size:2.2px;display:flex;align-items:center;justify-content:center">Details</div>
    <div class="a" style="right:5px;top:60px;width:22px;height:6px;background:var(--blue);border-radius:1px;font-size:2.2px;color:#fff;display:flex;align-items:center;justify-content:center">Add Account</div>
  </div>

  <h3 class="a" style="left:102px;top:226px;font-size:4.8px;font-weight:700;color:var(--ink)">Top Cashback Brokers This Month</h3>
  <div class="a" style="right:32px;top:227px;font-size:2.8px;color:var(--blue)">Compare all features</div>
  <div class="a table">
    <div class="table__row table__row--head"><span>BROKER</span><span>REGULATION</span><span>AVERAGE SPREAD</span><span>CASHBACK</span><span>ACTION</span><span></span></div>
    <div class="table__row"><span><b style="display:inline-block;width:4px;height:4px;background:var(--ink);vertical-align:middle;margin-right:2px"></b><b>Harbor Markets</b></span><span>AUR, CYR, FSR</span><span>0.0 Pips</span><span>Up to $8.00 / Lot</span><span><i class="btn-pill" style="font-style:normal;font-size:2.4px;padding:1px 3px">Sign Up</i></span><span></span></div>
    <div class="table__row"><span><b style="display:inline-block;width:4px;height:4px;background:var(--ink);vertical-align:middle;margin-right:2px"></b><b>Novexa</b></span><span>CYR, FCR, FSCR</span><span>0.1 Pips</span><span>Up to 33% Spread</span><span><i class="btn-pill" style="font-style:normal;font-size:2.4px;padding:1px 3px">Sign Up</i></span><span></span></div>
    <div class="table__row"><span><b style="display:inline-block;width:4px;height:4px;background:var(--ink);vertical-align:middle;margin-right:2px"></b><b>Peakstone</b></span><span>AUR, FCR, BAFR</span><span>0.0 Pips</span><span>$2.50 / Lot</span><span><i class="btn-pill" style="font-style:normal;font-size:2.4px;padding:1px 3px">Sign Up</i></span><span></span></div>
  </div>

  <div class="a cta">
    <div class="a" style="left:9px;top:9px;font-size:6px;font-weight:700;color:#fff">Can't Decide Which Broker To Choose?</div>
    <p class="a" style="left:9px;top:19px;width:110px;font-size:2.8px;line-height:1.5;color:#8a94a6">Our experts can help you find the best broker for your trading style and volume requirements. Use our side-by-side comparison tool or request a callback.</p>
    <div class="a" style="left:9px;top:42px;width:40px;height:9px;border-radius:1.5px;background:var(--blue);color:#fff;font-size:2.8px;font-weight:600;display:flex;align-items:center;justify-content:center">Compare Brokers</div>
    <div class="a" style="left:52px;top:42px;width:40px;height:9px;border-radius:1.5px;background:#1f293b;color:#fff;font-size:2.8px;display:flex;align-items:center;justify-content:center">Talk to an Advisor</div>
  </div>

  <div class="a" style="left:0;top:370px;width:100%;height:.6px;background:var(--line)"></div>
  <div class="a" style="left:61px;top:402px;font-size:5px;font-weight:800;color:var(--ink)">TRADEBACKS.</div>
  <p class="a" style="left:61px;top:410px;width:70px;font-size:2.8px;line-height:1.5;color:var(--muted)">The premier forex cashback service. We help traders globally recover their trading costs by providing high-performance daily cash rebates.</p>
  <div class="a" style="left:61px;top:436px;width:5px;height:5px;border-radius:50%;background:#e8eaee"></div>
  <div class="a" style="left:69px;top:436px;width:5px;height:5px;border-radius:50%;background:#e8eaee"></div>
  <div class="a footer-col" style="left:168px;top:402px"><h6>COMPANY</h6><p>About Us<br>Contact Support<br>News &amp; Blog<br>Careers</p></div>
  <div class="a footer-col" style="left:210px;top:402px"><h6>PRODUCT</h6><p>All Brokers<br>Rebate Calculator<br>How It Works<br>FAQ</p></div>
  <div class="a footer-col" style="left:253px;top:402px"><h6>LEGAL</h6><p>Terms of Service<br>Privacy Policy<br>Cookie Policy<br>Risk Disclosure</p></div>
  <div class="a" style="left:61px;top:482px;width:273px;height:.6px;background:var(--line)"></div>
  <div class="a" style="left:61px;top:487px;font-size:2.6px;font-weight:600;color:var(--ink)">© 2026 TRADEBACKS. ALL RIGHTS RESERVED.</div>
  <p class="a" style="left:61px;top:495px;width:273px;font-size:2.2px;line-height:1.6;color:#b3b8c0">Risk Warning: Trading foreign exchange and contracts for difference on margin carries a high level of risk and may not be suitable for all investors. Past performance is not indicative of future results. TRADEBACKS is not a broker and does not provide investment advice; rebates are paid from commissions received from partner brokers. Please ensure you fully understand the risks involved before trading.</p>
</section>

</body>
</html>
```